Quillon Media - Amazing Homepage

We would like to build an amazing homepage for our site. We will need it built in HTM5, so it works across devices and would like it to parallax scroll , so it looks amazing.
We are a digital media agency, that has recently launched. Our old site is self build through one of the standard web build sites. We will be hosting our new site independently.
This is our old site - www.quillon-media.com
The new site only really needs one scrolling page to explain what we do and have our contact details at the bottom.
We have a place to host it, once designed. So we can share with the final design for you to upload.
Attached are:
Brief
Logos and artwork
Our PowerPoint template to give you an idea of colours

```html
<!DOCTYPE html>
<html lang="en">
<head>
<meta charset="utf-8">
<title>Quillon Media – We Make Amazing</title>
<link rel="stylesheet" href="https://fonts.googleapis.com/css2?family=Raleway:wght@300;400&family=Comfortaa:wght@700&family=Architects+Daughter&family=Open+Sans:wght@400;600&display=swap">
<style>
:root{
  --ink:#2b2f3a;
  --navy:#1f2a44;
  --muted:#5b6270;
  --sky:#7fc5d9;
  --white:#ffffff;
  --sand:#ece9e4;
  --footer-text:#93bccb;
  --bar:#7fc5d9;
}
*{margin:0;padding:0;box-sizing:border-box}
html,body{width:1200px;height:3243px;overflow:hidden}
body{position:relative;background:var(--white);font-family:"Open Sans",Arial,sans-serif;color:var(--ink)}
section,footer{position:absolute;left:0;width:1200px}
.abs{position:absolute}

/* hero */
.hero{top:0;height:433px;background:linear-gradient(90deg,#0c1018 0%,#1a2230 45%,#2b3442 70%,#6b4a22 88%,#e0891e 100%)}
.hero-photo{left:150px;top:0;width:340px;height:433px;background:linear-gradient(180deg,#2a2f38,#111419)}
.hero-title{left:500px;top:155px;width:520px;text-align:center;color:var(--white);font-family:"Raleway",sans-serif;font-weight:300;font-size:46px;line-height:1.12}
.hero-title strong{font-family:"Comfortaa",sans-serif;font-weight:700;font-size:42px;letter-spacing:1px}

/* clarity */
.clarity{top:433px;height:471px}
.tablet-art{left:242px;top:105px;width:278px;height:175px;border-radius:14px;background:linear-gradient(160deg,#3b3f47,#15171b)}
.clarity-title{left:536px;top:105px;font-family:"Raleway",sans-serif;font-weight:300;font-size:31px;color:var(--ink);white-space:nowrap}
.clarity-list{left:556px;top:152px;width:440px;list-style:disc;font-size:11.5px;line-height:1.55;color:var(--muted)}
.clarity-note{left:556px;top:268px;font-size:14.5px;color:var(--muted)}
.motto{top:332px;left:0;width:1200px;text-align:center;font-family:"Architects Daughter",cursive;font-size:31px;color:var(--navy);letter-spacing:.5px}

/* fairness */
.fairness{top:904px;height:410px;background:radial-gradient(ellipse at 55% 55%,#f7fbfd 0%,#dcecf3 45%,#9fcfe0 100%)}
.sport-art{left:210px;top:6px;width:470px;height:352px;border-radius:20px;background:radial-gradient(circle at 40% 40%,rgba(63,170,210,.55),rgba(230,240,245,0))}
.fairness-text{left:525px;top:218px;width:520px;font-family:"Raleway",sans-serif;font-weight:300;font-size:30px;line-height:1.25;color:var(--ink)}

/* coup */
.coup{top:1314px;height:463px}
.coup-title{left:207px;top:120px;font-family:"Architects Daughter",cursive;font-size:32px;color:var(--ink);white-space:nowrap}
.coup-text{left:207px;top:170px;width:440px;font-size:15px;line-height:1.4;color:var(--ink)}
.coup-sign{left:207px;top:339px;font-family:"Architects Daughter",cursive;font-size:24px;color:var(--ink)}
.crowd-art{left:690px;top:66px;width:320px;height:350px;border-radius:16px;background:linear-gradient(180deg,#f1f1f1 0%,#cfcfcf 60%,#e9e9e9 100%)}

/* services */
.services{top:1777px;height:478px;background:var(--sky)}
.services-lead{top:66px;width:1200px;text-align:center;color:var(--white);font-size:18px}
.services-sub{top:108px;width:1200px;text-align:center;color:var(--white);font-size:14.5px;opacity:.95}
.service{top:178px;width:130px;text-align:center;color:var(--white);font-size:11px;font-weight:600;letter-spacing:.3px}
.service svg{display:block;margin:0 auto 14px}

/* results */
.results{top:2255px;height:692px}
.devices-art{left:324px;top:-146px;width:524px;height:290px;border-radius:18px;background:linear-gradient(160deg,#f4f5f6,#d9dcdf)}
.results-text{top:170px;left:290px;width:620px;text-align:center;font-family:"Raleway",sans-serif;font-weight:400;font-size:23px;line-height:1.35;color:var(--ink)}
.brand{top:333px;left:0;width:1200px;display:flex;justify-content:center;align-items:center;gap:16px}
.brand-name{font-family:"Raleway",sans-serif;font-weight:400;font-size:30px;letter-spacing:5px;color:var(--ink)}
.brand-tag{display:block;font-size:13px;letter-spacing:3px;margin-top:4px}
.brand-strap{top:440px;width:1200px;text-align:center;font-family:"Raleway",sans-serif;font-weight:300;font-size:52px;color:var(--ink)}
.clients{top:550px;left:200px;width:800px;display:flex;justify-content:space-between;align-items:center}
.client{font-family:"Raleway",sans-serif;font-weight:400;font-size:26px;color:var(--muted)}

/* contact */
.contact{top:2947px;height:248px;background:var(--sand);text-align:center;color:var(--footer-text)}
.contact-lead{position:absolute;top:65px;width:1200px;font-family:"Raleway",sans-serif;font-weight:400;font-size:24px}
.contact-info{position:absolute;top:132px;width:1200px;font-size:15px;line-height:1.75}

.legal{top:3195px;height:48px;background:var(--bar);color:var(--white);font-size:9px}
.legal-links{position:absolute;left:184px;top:18px}
.legal-copy{position:absolute;right:130px;top:18px}
</style>
</head>
<body>

<section class="hero">
  <div class="abs hero-photo" role="img" aria-label="Photograph of a thoughtful businessman in a dark suit"></div>
  <h1 class="abs hero-title">Got the feeling your<br><strong>DIGITAL MARKETING</strong><br>just isn’t quite ‘there’?</h1>
</section>

<section class="clarity">
  <div class="abs tablet-art" role="img" aria-label="Illustration of a tablet showing a project manager dashboard with team icons"></div>
  <h2 class="abs clarity-title">We keep fighting to give you clarity by:</h2>
  <ul class="abs clarity-list">
    <li>Creating a singular view of your digital eco system</li>
    <li>Reviewing how and why your money is being spent where it is</li>
    <li>Profiling your customers. Who doesn’t have 1000’s of different customers with different motivations, interests and value to the brand?</li>
    <li>Finding the best digital channels to communicate with them</li>
  </ul>
  <p class="abs clarity-note">Because everything is changing every day...exciting isn’t it!</p>
  <p class="abs motto">Never stop, never settle, always improve.&nbsp; Be amazing.</p>
</section>

<section class="fairness">
  <div class="abs sport-art" role="img" aria-label="Illustration of a football shirt, trophy, boots, foam finger and a GOAL sticker"></div>
  <p class="abs fairness-text">Every client deserves amazing work, regardless of the brand, it’s all real money</p>
</section>

<section class="coup">
  <div class="abs crowd-art" role="img" aria-label="Illustration of a small group of protesters holding blank placards"></div>
  <h2 class="abs coup-title">It’s time to start a coup...</h2>
  <p class="abs coup-text">there are too many large agency networks, too few agencies being transparent, too many putting quality of work second to income</p>
  <p class="abs coup-sign">Well, a very quiet coup.</p>
</section>

<section class="services">
  <p class="abs services-lead">We’ve yet to come across a client that wants to shrink...making us specialists in delivering growth!</p>
  <p class="abs services-sub">We’ve been optimising our digital knowledge for over 20 years and we genuinely know what we are talking about</p>

  <div class="abs service" style="left:179px">
    <svg width="74" height="74" viewBox="0 0 74 74"><circle cx="37" cy="37" r="35" fill="none" stroke="#fff" stroke-width="2"/><rect x="25" y="25" width="24" height="24" rx="2" fill="none" stroke="#fff" stroke-width="2"/><line x1="25" y1="31" x2="49" y2="31" stroke="#fff" stroke-width="2"/><rect x="30" y="36" width="6" height="8" fill="#fff"/></svg>PPC</div>
  <div class="abs service" style="left:320px">
    <svg width="74" height="74" viewBox="0 0 74 74"><circle cx="37" cy="37" r="35" fill="none" stroke="#fff" stroke-width="2"/><rect x="26" y="24" width="22" height="26" fill="none" stroke="#fff" stroke-width="2"/><rect x="30" y="38" width="3" height="8" fill="#fff"/><rect x="35" y="33" width="3" height="13" fill="#fff"/><rect x="40" y="36" width="3" height="10" fill="#fff"/></svg>SEO</div>
  <div class="abs service" style="left:465px">
    <svg width="74" height="74" viewBox="0 0 74 74"><circle cx="37" cy="37" r="35" fill="none" stroke="#fff" stroke-width="2"/><rect x="22" y="25" width="30" height="20" rx="2" fill="none" stroke="#fff" stroke-width="2"/><line x1="37" y1="45" x2="37" y2="50" stroke="#fff" stroke-width="2"/><line x1="30" y1="51" x2="44" y2="51" stroke="#fff" stroke-width="2"/></svg>DISPLAY</div>
  <div class="abs service" style="left:607px">
    <svg width="74" height="74" viewBox="0 0 74 74"><circle cx="37" cy="37" r="35" fill="none" stroke="#fff" stroke-width="2"/><circle cx="33" cy="30" r="5" fill="none" stroke="#fff" stroke-width="2"/><path d="M24 48c0-8 4-12 9-12s9 4 9 12" fill="none" stroke="#fff" stroke-width="2"/><circle cx="46" cy="44" r="5" fill="#fff"/></svg>PAID SOCIAL</div>
  <div class="abs service" style="left:748px">
    <svg width="74" height="74" viewBox="0 0 74 74"><circle cx="37" cy="37" r="35" fill="none" stroke="#fff" stroke-width="2"/><circle cx="37" cy="37" r="12" fill="none" stroke="#fff" stroke-width="2"/><circle cx="37" cy="37" r="4" fill="#fff"/><line x1="37" y1="21" x2="37" y2="25" stroke="#fff" stroke-width="3"/><line x1="37" y1="49" x2="37" y2="53" stroke="#fff" stroke-width="3"/><line x1="21" y1="37" x2="25" y2="37" stroke="#fff" stroke-width="3"/><line x1="49" y1="37" x2="53" y2="37" stroke="#fff" stroke-width="3"/></svg>DATA MANAGEMENT</div>
  <div class="abs service" style="left:893px">
    <svg width="74" height="74" viewBox="0 0 74 74"><circle cx="37" cy="37" r="35" fill="none" stroke="#fff" stroke-width="2"/><circle cx="37" cy="37" r="13" fill="none" stroke="#fff" stroke-width="2"/><circle cx="37" cy="37" r="7" fill="none" stroke="#fff" stroke-width="2"/><circle cx="37" cy="37" r="2" fill="#fff"/></svg>ATTRIBUTION</div>
</section>

<section class="results">
  <div class="abs devices-art" role="img" aria-label="Illustration of a tablet and a smartphone showing analytics charts"></div>
  <p class="abs results-text">Happily, we smash it for all our clients, with an average of 35% improvement in performance within the first quarter of working with us</p>
  <div class="abs brand">
    <svg width="64" height="64" viewBox="0 0 64 64" aria-hidden="true"><circle cx="32" cy="32" r="28" fill="none" stroke="#2b2f3a" stroke-width="2"/></svg>
    <div class="brand-name">QUILLON<span class="brand-tag">WE MAKE AMAZING</span></div>
  </div>
  <h2 class="abs brand-strap">We Make Amazing Logo</h2>
  <div class="abs clients">
    <span class="client">Calmafen</span>
    <span class="client">H&amp;R</span>
    <span class="client">Velora</span>
    <span class="client">Stagepass Tickets</span>
    <span class="client">Brindle</span>
  </div>
</section>

<footer class="contact">
  <p class="contact-lead">If you are still reading our rant then get in touch / follow us / let’s go for a coffee</p>
  <p class="contact-info">Our address is 14 Marlow Yard, London, E2 7QN<br>contact@quillon-media.com</p>
</footer>

<footer class="legal">
  <span class="legal-links">Terms of Use&nbsp; |&nbsp; Policy Policy</span>
  <span class="legal-copy">© Copyright 2014. All rights reserved</span>
</footer>

</body>
</html>
```